Re-vamp existing website :www.tallowmerefinch.com.au

We need a new website design for this website
www.tallowmerefinch.com.au.

"creating financial lightbulb moments"

Looking for something modern, corporate like this https://www.pebbleharbor.com.au

Imagery is important, showing really great images of what we do.

We want to keep the theme of:
Build Your Future
Invest in your Dreams
Grow You

We want a blog/opinion page on the website

Staying with our three logo colours throughout

Industry/Entity Type

Financial Service

Number of Pages Required

5+ page

```html
<!DOCTYPE html>
<html lang="en">
<head>
<meta charset="utf-8">
<title>Corvane Wealth — Financial Planning</title>
<link href="https://fonts.googleapis.com/css2?family=Open+Sans:wght@300;400;600;700&display=swap" rel="stylesheet">
<style>
:root{
  --green:#27b36a;
  --green-dark:#1f8f55;
  --navy:#1b2d52;
  --ink:#2b2f36;
  --muted:#8a9099;
  --line:#e3e6ea;
  --soft:#f1f2f4;
  --dark:#232629;
  --darker:#1a1c1e;
  --white:#ffffff;
}
*{box-sizing:border-box;margin:0;padding:0}
html,body{width:1200px;height:3724px;overflow:hidden}
body{font-family:"Open Sans",Arial,sans-serif;color:var(--ink);background:var(--white);font-size:11px;line-height:1.6}
.wrap{width:720px;margin:0 auto;position:relative;height:100%}
section,footer,header{position:relative;overflow:hidden}
.sec-title{font-size:20px;font-weight:300;letter-spacing:.5px;color:var(--green);text-transform:uppercase}
.sec-title b{font-weight:700;color:var(--ink)}
.sec-title::after{content:"";display:block;width:90px;height:2px;background:linear-gradient(90deg,var(--green) 30%,var(--line) 30%);margin-top:6px}
.light .sec-title b{color:var(--white)}
.btn{display:inline-block;font-size:9px;font-weight:700;letter-spacing:1px;padding:9px 26px;text-transform:uppercase}
.btn-green{background:var(--green);color:var(--white)}
.btn-white{background:var(--white);color:var(--navy)}
.photo{display:block}

/* hero */
.hero{height:560px;background:linear-gradient(120deg,#1a3566 0%,#1c4f6c 45%,#1e7f67 80%,#23986a 100%)}
.topbar{height:30px;display:flex;justify-content:space-between;align-items:center;padding:0 240px;color:#c7d3e4;font-size:8px}
.topbar .dots{display:flex;gap:6px}
.topbar .dots span{width:7px;height:7px;border-radius:50%;background:rgba(255,255,255,.6)}
.topbar .info{display:flex;gap:18px}
.nav{height:40px;display:flex;justify-content:space-between;align-items:center;padding:0 240px;border-top:1px solid rgba(255,255,255,.12)}
.brand{color:var(--white);font-weight:700;font-size:13px;display:flex;align-items:center;gap:6px}
.brand i{width:10px;height:10px;background:var(--green);display:block}
.menu{display:flex;gap:20px;align-items:center;font-size:8px;font-weight:600;color:var(--white);letter-spacing:.5px}
.menu .on{color:var(--green)}
.hero-photo{position:absolute;left:760px;top:190px;width:200px;height:370px;background:linear-gradient(180deg,#3d5f86,#c9d7e6 55%,#9fb3c9);border-radius:90px 90px 0 0}
.hero-copy{position:absolute;left:240px;top:258px;color:var(--white)}
.hero-copy h1{font-size:34px;font-weight:400;letter-spacing:-.3px}
.hero-copy p{font-size:10px;color:#d6e2ee;width:300px;margin:6px 0 18px}
.hero-copy .btn{margin-right:10px;padding:8px 22px}
.arrow{position:absolute;top:258px;width:26px;height:26px;border:1px solid rgba(255,255,255,.5);border-radius:50%}
.arrow.l{left:60px}.arrow.r{right:60px}
.hero-down{position:absolute;left:586px;bottom:-14px;width:28px;height:28px;border-radius:50%;background:var(--white);border:1px solid var(--line)}

/* about */
.about{height:320px}
.about .wrap{padding-top:64px}
.about-text{width:400px;margin-top:16px}
.about-text h3{font-size:11px;font-weight:700;margin-bottom:10px}
.about-text p{color:var(--muted);font-size:9px;margin-bottom:8px}
.about-text a{font-size:9px;font-weight:600;color:var(--ink)}
.about-photo{position:absolute;right:8px;top:68px;width:284px;height:200px;background:linear-gradient(135deg,#3a4a5c,#8c9aa8 60%,#c7d0d8)}

/* services */
.services{height:440px}
.services .wrap{padding-top:24px}
.tiles{position:absolute;top:80px;left:0;width:712px;height:348px}
.tile{position:absolute;color:var(--white);font-size:8px;font-weight:700;letter-spacing:.5px;text-transform:uppercase;display:flex;align-items:center;justify-content:center;text-align:center}
.tile.g{background:linear-gradient(135deg,#3ec482,#1f9a5a)}
.tile.b{background:var(--navy);flex-direction:column;text-transform:none;font-size:11px}
.tile.b small{font-weight:400;font-size:8px;color:#aebad0}
.tile .ic{position:absolute;right:8px;top:8px;width:18px;height:18px;border:1px solid rgba(255,255,255,.7)}

/* role */
.role{height:280px}
.role .wrap{padding-top:18px}
.cards{display:flex;gap:8px;margin-top:40px}
.card{width:232px;height:140px;border:1px solid var(--line);position:relative;padding:34px 16px 0}
.card .badge{position:absolute;left:100px;top:-18px;width:34px;height:34px;border-radius:50%;background:var(--green);display:flex;align-items:center;justify-content:center}
.card .badge.grey{background:#9aa1aa}
.card h4{font-size:10px;font-weight:700}
.card .num{position:absolute;right:14px;top:30px;font-size:18px;color:#e4e7ea;font-weight:700}
.card p{font-size:8.5px;color:var(--muted);margin-top:8px}

/* call back */
.callback{height:350px;background:linear-gradient(180deg,#2c2f33,#1f2124)}
.callback .wrap{padding-top:52px}
.cb-text{position:absolute;left:0;top:116px;width:220px;color:#a7acb3;font-size:8.5px}
.form{position:absolute;left:240px;top:116px;width:472px;display:grid;grid-template-columns:1fr 1fr;gap:10px}
.field{height:28px;border:1px solid #4a4e54;background:rgba(255,255,255,.04);color:#b9bec4;font-size:8px;padding:0 10px;display:flex;align-items:center;justify-content:space-between}
.field.area{grid-column:1/3;height:64px;align-items:flex-start;padding-top:8px}
.form .btn{grid-column:1/3;justify-self:center;margin-top:6px}

/* figures */
.figures{height:270px}
.figures .wrap{padding-top:50px}
.stats{display:flex;margin-top:40px}
.stat{width:178px;text-align:center}
.stat svg{display:block;margin:0 auto 12px}
.stat strong{display:block;font-size:20px;font-weight:700}
.stat span{font-size:8px;color:var(--muted)}

/* testimonials */
.testimonials{height:250px}
.testimonials .wrap{padding-top:20px}
.quote-box{position:absolute;top:80px;left:0;width:712px;height:160px;background:var(--soft);text-align:center;padding-top:42px}
.avatar{position:absolute;left:336px;top:-20px;width:40px;height:40px;border-radius:50%;background:linear-gradient(180deg,#b9c2cc,#6c7887);border:3px solid var(--white)}
.quote-box h5{font-size:10px;font-weight:700}
.quote-box em{display:block;font-style:normal;color:var(--green);font-size:8px}
.quote-box p{font-size:8.5px;color:var(--muted);width:440px;margin:10px auto}
.pager{display:flex;gap:5px;justify-content:center}
.pager i{width:6px;height:6px;border-radius:50%;background:#c9cdd2}
.pager i.on{background:var(--green)}

/* team */
.team{height:330px}
.team .wrap{padding-top:18px}
.members{display:flex;gap:24px;margin-top:36px}
.member{width:160px}
.member .photo{height:168px;background:linear-gradient(180deg,#d9dde2,#9aa4af);position:relative}
.member .photo.dark{background:linear-gradient(180deg,#3a3d42,#25272a)}
.member .soc{position:absolute;left:50px;top:76px;display:flex;gap:8px}
.member .soc i{width:14px;height:14px;border-radius:50%;border:1px solid rgba(255,255,255,.8)}
.member h5{font-size:9px;font-weight:700;margin-top:8px}
.member span{font-size:8px;color:var(--muted)}
.team .pager{margin-top:14px}

/* blogs */
.blogs{height:400px;background:var(--soft)}
.blogs .wrap{padding-top:48px}
.blog-nav{position:absolute;right:8px;top:58px;font-size:8px;font-weight:700;display:flex;gap:12px}
.blog-nav span:last-child{color:var(--muted)}
.posts{display:flex;gap:40px;margin-top:32px}
.post{width:336px}
.post .photo{height:192px;position:relative;background:linear-gradient(135deg,#6e7f93,#c6d0da 60%,#e3e8ec)}
.post .photo.b{background:linear-gradient(135deg,#3f4a57,#7f8d99 55%,#b9c3cb)}
.date{position:absolute;left:12px;top:0;width:34px;height:40px;background:var(--green);color:var(--white);font-size:8px;font-weight:700;text-align:center;line-height:1.2;padding-top:8px}
.tag{position:absolute;right:0;bottom:10px;background:var(--white);font-size:7px;font-weight:600;padding:4px 10px}
.post h4{font-size:9.5px;font-weight:700;margin-top:12px}
.post p{font-size:8px;color:var(--muted);margin:4px 0}
.post a{font-size:8px;font-weight:700;color:var(--green)}

/* partners */
.partners{height:210px}
.partners .wrap{padding-top:46px}
.logos{display:flex;justify-content:space-between;margin-top:30px;padding:0 10px}
.logos i{width:56px;height:56px;border-radius:50%;border:2px solid #c7ccd1;display:block}
.partners .blog-nav{top:56px}

/* footer */
.footer{height:314px;background:var(--darker);color:#8e949b;font-size:8px}
.footer .wrap{padding-top:44px}
.cols{display:flex;gap:28px}
.col h6{color:var(--white);font-size:9px;font-weight:700;letter-spacing:.5px;margin-bottom:14px}
.col.about-f{width:150px;padding-top:48px}
.col.links{width:150px}
.links ul{list-style:none;columns:2;column-gap:14px}
.links li{margin-bottom:8px}
.col.recent{width:150px}
.rp{display:flex;gap:8px;margin-bottom:12px}
.rp i{width:34px;height:30px;background:linear-gradient(135deg,#4a525c,#8f99a3);flex:none}
.rp b{display:block;color:#c9ced3;font-weight:600}
.col.sub{width:160px}
.sub-form{display:flex;margin-top:10px}
.sub-form span{flex:1;height:24px;background:#2c2f33;padding:6px 8px}
.sub-form b{width:28px;background:var(--green)}
.bottom{position:absolute;left:0;right:0;bottom:0;height:40px;border-top:1px solid #2e3135;display:flex;justify-content:space-between;align-items:center;padding:0 248px;font-size:7.5px}
.bottom .dots{display:flex;gap:8px}
.bottom .dots i{width:8px;height:8px;border-radius:50%;background:#555a60}
</style>
</head>
<body>

<header class="hero">
  <div class="topbar">
    <div class="dots"><span></span><span></span><span></span><span></span><span></span></div>
    <div class="info"><span>hello@corvanewealth.example</span><span>(02) 5550 1842</span><span>Login</span></div>
  </div>
  <nav class="nav">
    <div class="brand"><i></i>Corvane Wealth</div>
    <div class="menu">
      <span>HOME</span><span>ABOUT</span><span>SERVICES</span><span class="on">PORTFOLIO</span><span>NEWS</span><span>BLOG</span><span>CONTACT</span>
      <svg width="10" height="10" viewBox="0 0 10 10"><circle cx="4" cy="4" r="3" fill="none" stroke="#fff"/><line x1="6.3" y1="6.3" x2="9" y2="9" stroke="#fff"/></svg>
      <svg width="10" height="10" viewBox="0 0 10 10"><path d="M2 3h6l-1 6H3z" fill="none" stroke="#fff"/></svg>
    </div>
  </nav>
  <div class="hero-photo" role="img" aria-label="Financial adviser in a white shirt and tie, arms folded"></div>
  <div class="hero-copy">
    <h1>We Provide Financial Planning</h1>
    <p>Creating financial lightbulb moments: clear advice that helps you build your future, invest in your dreams and grow.</p>
    <span class="btn btn-white">Contact</span><span class="btn btn-green">Details</span>
  </div>
  <span class="arrow l"></span><span class="arrow r"></span>
  <span class="hero-down"></span>
</header>

<section class="about">
  <div class="wrap">
    <h2 class="sec-title">About <b>Us</b></h2>
    <div class="about-text">
      <h3>20 Year Of Experience</h3>
      <p>For two decades we have guided families and business owners through every stage of their financial life, from first home loans to retirement planning and wealth protection.</p>
      <p>Our advisers listen first, then build a plan that fits your goals and grows with you over time.</p>
      <a>Read More ›</a>
    </div>
    <div class="about-photo" role="img" aria-label="Team of advisers meeting around a laptop"></div>
  </div>
</section>

<section class="services">
  <div class="wrap">
    <h2 class="sec-title">Our <b>Sevices</b></h2>
    <div class="tiles">
      <div class="tile g" style="left:0;top:0;width:288px;height:168px" role="img" aria-label="Financial planning photo with green overlay">Financial Planning<span class="ic"></span></div>
      <div class="tile b" style="left:308px;top:0;width:224px;height:168px">Commodities<small>Varieties Trading</small><span class="ic"></span></div>
      <div class="tile g" style="left:552px;top:0;width:160px;height:348px" role="img" aria-label="Mortgage broker photo with green overlay">Mortgage Broker</div>
      <div class="tile g" style="left:0;top:188px;width:532px;height:160px" role="img" aria-label="Super and investing photo with green overlay">Super &amp; Investing</div>
    </div>
  </div>
</section>

<section class="role">
  <div class="wrap">
    <h2 class="sec-title">Role of <b>Wage</b></h2>
    <div class="cards">
      <div class="card"><span class="badge"><svg width="14" height="14" viewBox="0 0 14 14"><path d="M2 11l4-4 3 3 4-6" fill="none" stroke="#fff" stroke-width="1.5"/></svg></span><span class="num">01</span><h4>Investment Planning</h4><p>We build a balanced portfolio around your goals, timeline and comfort with risk.</p></div>
      <div class="card"><span class="badge grey"><svg width="14" height="14" viewBox="0 0 14 14"><path d="M7 1l5 2v4c0 3-2 5-5 6-3-1-5-3-5-6V3z" fill="none" stroke="#fff" stroke-width="1.5"/></svg></span><span class="num">02</span><h4>Insurance Policies</h4><p>Protect your income, family and assets with cover that suits the way you live.</p></div>
      <div class="card"><span class="badge"><svg width="14" height="14" viewBox="0 0 14 14"><path d="M1 7a6 6 0 0 1 12 0M7 7v5" fill="none" stroke="#fff" stroke-width="1.5"/></svg></span><span class="num">03</span><h4>Trading Policies</h4><p>Clear trading rules and regular reviews keep your strategy on track in any market.</p></div>
    </div>
  </div>
</section>

<section class="callback light">
  <div class="wrap">
    <h2 class="sec-title">Get a Call <b>Back</b></h2>
    <p class="cb-text">Leave your details and one of our advisers will call you back within one business day. We will talk through your situation, answer your questions and explain how we can help you build, invest and grow with no obligation.</p>
    <div class="form">
      <span class="field">Name</span><span class="field">E-mail</span>
      <span class="field">Phone Number</span><span class="field">Consult Me Anytime <span>▾</span></span>
      <span class="field area">Message</span>
      <span class="btn btn-green">Submit Now</span>
    </div>
  </div>
</section>

<section class="figures">
  <div class="wrap">
    <h2 class="sec-title">Work in <b>Figures</b></h2>
    <div class="stats">
      <div class="stat"><svg width="28" height="28" viewBox="0 0 28 28" fill="none" stroke="#27b36a" stroke-width="1.5"><circle cx="14" cy="9" r="5"/><path d="M4 25c1-6 5-9 10-9s9 3 10 9"/></svg><strong>4600+</strong><span>Experienced Advisors</span></div>
      <div class="stat"><svg width="28" height="28" viewBox="0 0 28 28" fill="none" stroke="#27b36a" stroke-width="1.5"><circle cx="14" cy="14" r="11"/><path d="M3 14h22M14 3c4 4 4 18 0 22M14 3c-4 4-4 18 0 22"/></svg><strong>4030+</strong><span>Worldwide Locations</span></div>
      <div class="stat"><svg width="28" height="28" viewBox="0 0 28 28" fill="none" stroke="#27b36a" stroke-width="1.5"><rect x="5" y="4" width="18" height="21"/><path d="M9 19v-4M14 19v-8M19 19v-6"/></svg><strong>0256</strong><span>Years of Experience</span></div>
      <div class="stat"><svg width="28" height="28" viewBox="0 0 28 28" fill="none" stroke="#27b36a" stroke-width="1.5"><path d="M14 24S4 17 4 10a5 5 0 0 1 10-2 5 5 0 0 1 10 2c0 7-10 14-10 14z"/></svg><strong>8549+</strong><span>Satisfied Customers</span></div>
    </div>
  </div>
</section>

<section class="testimonials">
  <div class="wrap">
    <h2 class="sec-title">Our <b>Testimonials</b></h2>
    <div class="quote-box">
      <span class="avatar" role="img" aria-label="Client portrait"></span>
      <h5>Jonathan Reed</h5>
      <em>Small Business Owner</em>
      <p>The team made our finances simple. We finally have a plan for the business, our home loan and retirement, and we check in every year to keep it on track.</p>
      <div class="pager"><i class="on"></i><i></i><i></i></div>
    </div>
  </div>
</section>

<section class="team">
  <div class="wrap">
    <h2 class="sec-title">Our <b>Team</b></h2>
    <div class="members">
      <div class="member"><div class="photo" role="img" aria-label="Portrait of senior adviser"></div><h5>Brett Lennard</h5><span>Senior Adviser</span></div>
      <div class="member"><div class="photo" role="img" aria-label="Portrait of mortgage specialist"></div><h5>Robyn Palmer</h5><span>Mortgage Specialist</span></div>
      <div class="member"><div class="photo dark" role="img" aria-label="Portrait of investment manager"><span class="soc"><i></i><i></i><i></i></span></div><h5>Edwin Marsh</h5><span>Investment Manager</span></div>
      <div class="member"><div class="photo" role="img" aria-label="Portrait of insurance adviser"></div><h5>Charles Norton</h5><span>Insurance Adviser</span></div>
    </div>
    <div class="pager"><i class="on"></i><i></i><i></i></div>
  </div>
</section>

<section class="blogs">
  <div class="wrap">
    <h2 class="sec-title">Our <b>Blogs</b></h2>
    <div class="blog-nav"><span>PREV</span><span>NEXT</span></div>
    <div class="posts">
      <div class="post"><div class="photo" role="img" aria-label="Charts and documents on a desk"><span class="date">12<br>MAR</span><span class="tag">Financial Advantage</span></div><h4>Solution for Improve your all business growth</h4><p>Simple steps to manage cash flow, plan ahead and grow your business with confidence.</p><a>Read More ›</a></div>
      <div class="post"><div class="photo b" role="img" aria-label="Advisers reviewing figures on a laptop"><span class="date">18<br>MAR</span><span class="tag">Financial Advantage</span></div><h4>Solution for Improve your all business growth</h4><p>How a regular review with your adviser keeps your investments aligned with your goals.</p><a>Read More ›</a></div>
    </div>
  </div>
</section>

<section class="partners">
  <div class="wrap">
    <h2 class="sec-title">Our <b>Partners</b></h2>
    <div class="blog-nav"><span>PREV</span><span>NEXT</span></div>
    <div class="logos"><i></i><i></i><i></i><i></i><i></i><i></i></div>
  </div>
</section>

<footer class="footer">
  <div class="wrap">
    <div class="cols">
      <div class="col about-f"><p>Helping Australians build their future, invest in their dreams and grow with clear, honest advice.</p><p style="margin-top:10px">(02) 5550 1842<br>hello@corvanewealth.example</p></div>
      <div class="col links"><h6>USEFUL LINKS</h6><ul><li>Home</li><li>About Us</li><li>Services</li><li>Portfolio</li><li>Our Team</li><li>Blog</li><li>News</li><li>Careers</li><li>Contact</li><li>Support</li></ul></div>
      <div class="col recent"><h6>RECENT POST</h6>
        <div class="rp"><i role="img" aria-label="Post thumbnail"></i><span><b>Planning for retirement</b>12 March</span></div>
        <div class="rp"><i role="img" aria-label="Post thumbnail"></i><span><b>First home buyer tips</b>08 March</span></div>
      </div>
      <div class="col sub"><h6>SUBSCRIBE US</h6><p>Get our latest insights and news straight to your inbox.</p><div class="sub-form"><span>Email address</span><b></b></div></div>
    </div>
  </div>
  <div class="bottom"><span>Copyright © 2024 Corvane Wealth. All Rights Reserved.</span><div class="dots"><i></i><i></i><i></i><i></i><i></i></div></div>
</footer>

</body>
</html>
```